Silver Brook Constructions Ltd Stationary
business cards, stationary etc.
Silver Brook Constructions Ltd Stationary - Construction
Creative Brief
Simple
Dalton Wexford
4816 Ardmore Rd. Victoria B.C. V8N 4K7
250-384-6252 could we put this number under office instead of phone
222-222-2222 temporary until I get new number
dalton@silverbrookconstructions.example
www.silverbrookconstructions.example
We would like designs for business cards , envelopes, letterhead, thank-you cards with evelopes, fax cover sheet, and presentation folder. Thank you
information should be on the back of the card along with some clean lines and simplicity while keeping a very professional feel

```html
<!DOCTYPE html>
<html lang="en">
<head>
<meta charset="utf-8">
<title>Silver Brook Constructions Ltd — Business Card</title>
<link href="https://fonts.googleapis.com/css2?family=Cinzel:wght@600&family=Crimson+Text:wght@400&display=swap" rel="stylesheet">
<style>
  :root {
    --backdrop: #e8e5e0;
    --card: #ffffff;
    --brand-green: #6d8c3c;
    --ink: #111111;
    --text: #3d3d3d;
    --rule: #9a9a9a;
    --ring: #b9bcbf;
  }
  * { margin: 0; padding: 0; box-sizing: border-box; }
  html, body { width: 1200px; height: 852px; overflow: hidden; }
  body { background: var(--backdrop); position: relative; font-family: "Crimson Text", Georgia, serif; }

  .card {
    position: absolute;
    width: 540px; height: 310px;
    background: var(--card);
    border-radius: 20px;
    overflow: hidden;
    box-shadow: 0 6px 18px rgba(0,0,0,0.18);
  }
  .card-front { left: 50px; top: 120px; }
  .card-back { left: 610px; top: 420px; }

  .swoosh { position: absolute; left: 0; bottom: 0; width: 540px; height: 310px; }
  .swoosh .band { fill: var(--brand-green); }
  .swoosh .base { fill: var(--ink); }

  /* front */
  .brand-mark {
    position: absolute; left: 50%; top: 38px; transform: translateX(-50%);
    width: 74px; height: 74px; border-radius: 50%;
    border: 8px solid var(--ring);
  }
  .brand-name {
    position: absolute; left: 0; right: 0; top: 128px;
    text-align: center;
    font-family: "Cinzel", Georgia, serif; font-weight: 600;
    font-size: 24px; line-height: 1.15; letter-spacing: 1px;
    color: var(--ink);
  }

  /* back */
  .holder-name {
    position: absolute; left: 0; right: 0; top: 62px;
    text-align: center;
    font-family: "Cinzel", Georgia, serif; font-weight: 600;
    font-size: 20px; letter-spacing: 1px;
    color: var(--brand-green);
  }
  .address {
    position: absolute; right: 296px; top: 130px;
    text-align: right; font-size: 13px; line-height: 1.35; color: var(--text);
  }
  .divider {
    position: absolute; left: 258px; top: 104px; width: 1px; height: 104px;
    background: var(--rule);
  }
  .contacts {
    position: absolute; left: 270px; top: 104px;
    list-style: none; font-size: 13px; line-height: 1; color: var(--text);
  }
  .contacts li { display: flex; align-items: center; gap: 7px; height: 20px; }
  .contacts svg { width: 11px; height: 11px; fill: var(--rule); flex: none; }
</style>
</head>
<body>

<section class="card card-front" aria-label="Business card front">
  <div class="brand-mark"></div>
  <p class="brand-name">Silver Brook<br>Constructions Ltd</p>
  <svg class="swoosh" viewBox="0 0 540 310" aria-hidden="true">
    <path class="band" d="M0,236 C170,276 360,232 540,196 L540,210 C360,244 170,292 0,250 Z"/>
    <path class="base" d="M0,262 C180,304 360,256 540,218 L540,310 L0,310 Z"/>
  </svg>
</section>

<section class="card card-back" aria-label="Business card back">
  <p class="holder-name">Dalton Wexford</p>
  <p class="address">4816 Ardmore Rd.<br>Victoria B.C. V8N 4K7</p>
  <div class="divider"></div>
  <ul class="contacts">
    <li><svg viewBox="0 0 12 12"><path d="M2.5 0.5 L4.5 0.5 L5.2 3.3 L3.8 4.4 C4.5 6 6 7.5 7.6 8.2 L8.7 6.8 L11.5 7.5 L11.5 9.5 C11.5 10.8 10.6 11.5 9.5 11.5 C4.5 11 1 7.5 0.5 2.5 C0.5 1.4 1.2 0.5 2.5 0.5 Z"/></svg>250-384-6252</li>
    <li><svg viewBox="0 0 12 12"><rect x="3" y="0.5" width="6" height="11" rx="1.2"/></svg>222-222-2222</li>
    <li><svg viewBox="0 0 12 12"><circle cx="6" cy="6" r="5.5"/></svg>dalton@silverbrookconstructions.example</li>
    <li><svg viewBox="0 0 12 12"><circle cx="6" cy="6" r="5.5"/></svg>www.silverbrookconstructions.example</li>
  </ul>
  <svg class="swoosh" viewBox="0 0 540 310" aria-hidden="true">
    <path class="band" d="M0,236 C170,276 360,232 540,196 L540,210 C360,244 170,292 0,250 Z"/>
    <path class="base" d="M0,262 C180,304 360,256 540,218 L540,310 L0,310 Z"/>
  </svg>
</section>

</body>
</html>
```